Wholesaler needs a bag design for cassava flour

I need design for a package bag to pack cassava flour (white powder). This flower is made from manioc and is very much used by African countries. I want to make packages of 0.5kg with 160mm base to 230mm height. I would like ta package to have clear parts so that customers can see the quality of the product. The brand name of the product is " MIRAVO " and the name of the product in Portuguese is "Fuba de Bombó". I want the design to be simple not many colors and attractive.
The design should have a front page and a back page. The front side I would like to have the brand, the name of the product and a simple design while on the back side it should have the space to fill with the nutrition facts, our company information, bar code and other information demanded by EU regulation
African Communities in Portugal
Wholesale

```html
<!DOCTYPE html>
<html lang="pt">
<head>
<meta charset="UTF-8">
<title>MIRAVO – Fuba de Bombó 500g</title>
<link href="https://fonts.googleapis.com/css2?family=Montserrat:wght@500;800&family=Oswald:wght@500&display=swap" rel="stylesheet">
<style>
  :root {
    --bg: #f4f4f4;
    --kraft-light: #e2c29c;
    --kraft: #cfa77c;
    --kraft-dark: #b58b61;
    --cocoa: #5a4327;
    --cocoa-deep: #4a3520;
    --cream: #edcfac;
    --brand: #5b2e14;
    --window: #ffffff;
    --string: #e9e9e9;
  }
  html, body {
    margin: 0;
    padding: 0;
    width: 1200px;
    height: 1200px;
    overflow: hidden;
    background: var(--bg);
  }
  .bag-front {
    position: absolute;
    left: 300px;
    top: 90px;
    width: 600px;
    height: 1020px;
  }
  .bag-art {
    position: absolute;
    inset: 0;
  }
  .brand {
    position: absolute;
    left: 70px;
    top: 250px;
    width: 220px;
    display: flex;
    flex-direction: column;
    align-items: center;
    gap: 18px;
  }
  .brand-dot {
    width: 70px;
    height: 70px;
    border-radius: 50%;
    background: var(--brand);
    opacity: .85;
  }
  .brand-name {
    font-family: "Montserrat", sans-serif;
    font-weight: 500;
    font-size: 32px;
    letter-spacing: 2px;
    color: var(--brand);
  }
  .product-name {
    position: absolute;
    left: 320px;
    top: 240px;
    margin: 0;
    font-family: "Montserrat", sans-serif;
    font-weight: 800;
    font-size: 54px;
    line-height: 1.25;
    color: var(--cream);
  }
  .product-name span { display: block; padding-left: 14px; }
  .net-weight {
    position: absolute;
    left: 150px;
    top: 940px;
    font-family: "Oswald", sans-serif;
    font-weight: 500;
    font-size: 20px;
    color: var(--cocoa-deep);
  }
</style>
</head>
<body>
  <div class="bag-front">
    <svg class="bag-art" width="600" height="1020" viewBox="0 0 600 1020" aria-hidden="true">
      <defs>
        <linearGradient id="kraftShade" x1="0" y1="0" x2="1" y2="0">
          <stop offset="0" stop-color="var(--kraft-dark)"/>
          <stop offset=".55" stop-color="var(--kraft-light)"/>
          <stop offset="1" stop-color="var(--kraft)"/>
        </linearGradient>
      </defs>
      <rect class="panel-cocoa" x="0" y="0" width="600" height="1020" fill="var(--cocoa)"/>
      <polygon class="panel-kraft" points="0,0 260,0 300,1020 0,1020" fill="url(#kraftShade)"/>
      <line class="top-stitch" x1="0" y1="110" x2="600" y2="110" stroke="var(--string)" stroke-width="3" stroke-dasharray="14 4" opacity=".8"/>
      <rect class="product-window" x="340" y="640" width="210" height="300" rx="18" fill="var(--window)"/>
    </svg>

    <div class="brand">
      <div class="brand-dot"></div>
      <div class="brand-name">MIRAVO</div>
    </div>

    <h1 class="product-name">Fuba de<span>Bombó</span></h1>

    <div class="net-weight">500GR</div>
  </div>
</body>
</html>
```